Banner Ad Design Project

I require banner ad designs with the below wording.

1. Join Today and Make Money Tomorrow. Unlimited Income. Click Here Now

2. I lost my job. Now I Make Over $5,000 Per Week From Home. You Can Too. Free Info, Apply Now

I require sizes: 300x250 and 728x90 and 468x60 and 120x240

The design should communicate legitimate, accredited, online business.

Industry/Entity Type

Business

Requirements
Should not have
• Creative attributes to avoid*
Phone numbers in creative
Creative with no click buttons
Interactive creative
Brand messaging with no call to action
Creative with long looping times

```html
<!DOCTYPE html>
<html lang="en">
<head>
<meta charset="utf-8">
<title>Join Today Banner</title>
<link rel="stylesheet" href="https://fonts.googleapis.com/css2?family=Bebas+Neue&family=Roboto+Slab:wght@300;700&display=swap">
<style>
  :root {
    --stage: #000000;
    --card: #ffffff;
    --headline-red: #d11f49;
    --headline-red-dark: #b8173d;
    --headline-cream: #ecdf9c;
    --headline-white: #ffffff;
    --slate: #555555;
    --button-top: #35a9e6;
    --button-bottom: #1769b3;
    --photo-warm: #c9a48f;
    --photo-green: #a9b59a;
    --photo-blue: #8fb2d8;
  }
  html, body {
    margin: 0;
    padding: 0;
    width: 1200px;
    height: 711px;
    overflow: hidden;
    background: var(--stage);
  }
  .banner {
    position: absolute;
    left: 303px;
    top: 99px;
    width: 585px;
    height: 488px;
    background: var(--card);
    overflow: hidden;
  }
  .headline-panel {
    position: absolute;
    left: 141px;
    top: 9px;
    width: 435px;
    height: 232px;
    background: linear-gradient(180deg, var(--headline-red) 0%, var(--headline-red-dark) 100%);
    border-top-right-radius: 10px;
  }
  .hero-photo {
    position: absolute;
    left: 0;
    top: 0;
    width: 215px;
    height: 488px;
    background: linear-gradient(180deg, var(--photo-warm) 0%, var(--photo-green) 50%, var(--photo-blue) 100%);
  }
  .copy-column {
    position: absolute;
    left: 222px;
    width: 330px;
    text-align: center;
    white-space: nowrap;
    line-height: 1;
    margin: 0;
  }
  .headline-primary {
    top: 12px;
    font-family: "Bebas Neue", "Arial Narrow", sans-serif;
    font-size: 108px;
    font-weight: 400;
    color: var(--headline-cream);
    letter-spacing: -1px;
  }
  .headline-secondary {
    font-family: "Bebas Neue", "Arial Narrow", sans-serif;
    font-size: 64px;
    font-weight: 400;
    color: var(--headline-white);
    letter-spacing: -0.5px;
  }
  .headline-secondary.line-one { top: 116px; }
  .headline-secondary.line-two { top: 174px; }
  .offer-small {
    top: 253px;
    font-family: "Roboto Slab", Georgia, serif;
    font-weight: 300;
    font-size: 45px;
    color: var(--slate);
  }
  .offer-large {
    top: 291px;
    font-family: "Roboto Slab", Georgia, serif;
    font-weight: 300;
    font-size: 68px;
    color: var(--slate);
  }
  .cta-button {
    position: absolute;
    left: 253px;
    top: 392px;
    width: 265px;
    height: 68px;
    border-radius: 10px;
    background: linear-gradient(180deg, var(--button-top) 0%, var(--button-bottom) 100%);
    box-shadow: 0 2px 4px rgba(0,0,0,0.3);
    color: var(--headline-white);
    font-family: "Roboto Slab", Georgia, serif;
    font-weight: 700;
    font-size: 26px;
    line-height: 68px;
    text-align: center;
    text-decoration: none;
  }
</style>
</head>
<body>
  <div class="banner">
    <div class="headline-panel"></div>
    <div class="hero-photo" role="img" aria-label="Photo of an excited woman in a striped blue shirt hugging a large pile of dollar bills"></div>
    <h1 class="copy-column headline-primary">JOIN TODAY</h1>
    <p class="copy-column headline-secondary line-one">AND MAKE MONEY</p>
    <p class="copy-column headline-secondary line-two">TOMORROW</p>
    <p class="copy-column offer-small">UNLIMITED</p>
    <p class="copy-column offer-large">INCOME</p>
    <a class="cta-button" href="#">Click Here Now</a>
  </div>
</body>
</html>
```